Hale & Whitcombe Family Practice Ad

Hi,my name is Dr. Talia P. Whitcombe, and I am a new physician returning home to start working in family medicine. I am wanting an ad that, attracts new patients to our practice, men and women of all ages.
Our practice is located in the country, and has long been established as part of the Southampton community. I am working alongside a seasoned clinician who has been in practice for almost 20 years.
Updates
Project Deadline Extended
Reason: Wanting to give designers more time to make revisions.
Project Deadline Extended
Reason: Last minute changes.
Target Market(s)
Males and Females of all ages
Industry/Entity Type
Community
Requirements
Must have
- Logo design, "Hale & Whitcombe Family Practice", uploaded files below.
Office Address:
47 Fennel Lane, Southampton TQ19
Telephone: 568-9072
Office Hours: Tuesday - Friday
Nice to have
- An image that captures our slogan: Restore, Refresh, Renew.

```html
<!DOCTYPE html>
<html lang="en">
<head>
<meta charset="utf-8">
<title>Hale &amp; Whitcombe Family Practice Ad</title>
<link rel="stylesheet" href="https://fonts.googleapis.com/css2?family=Jost:wght@500&family=Roboto+Condensed:wght@400&family=Arimo:ital,wght@1,700&family=Montserrat:wght@800&display=swap">
<style>
  :root {
    --navy: #27348b;
    --green: #0aa84f;
    --purple: #7b74b8;
    --ink: #111111;
    --paper: #ffffff;
    --frame: #1a1a1a;
  }
  * { margin: 0; padding: 0; box-sizing: border-box; }
  html, body { width: 1200px; height: 900px; overflow: hidden; background: var(--paper); }
  .canvas { position: relative; width: 1200px; height: 900px; }
  .ad {
    position: absolute; left: 299px; top: 149px; width: 603px; height: 602px;
    background: var(--paper); border: 2px solid var(--frame);
    box-shadow: 3px 4px 6px rgba(0,0,0,0.3); overflow: hidden;
  }
  .side-band { position: absolute; right: 0; top: 0; width: 81px; height: 100%; background: var(--green); }
  .practice-name {
    position: absolute; right: 100px; top: 30px;
    font-family: "Jost", sans-serif; font-weight: 500; color: var(--navy);
    text-align: right; line-height: 1; white-space: nowrap;
  }
  .practice-name .line-main { display: block; font-size: 52px; letter-spacing: -1.5px; }
  .practice-name .line-sub { display: block; font-size: 44px; margin-top: 12px; }
  .name-mark {
    position: absolute; left: 40px; top: 170px; width: 150px; height: 150px;
    border-radius: 50%; background: var(--purple);
  }
  .slogan {
    position: absolute; left: 296px; top: 176px; list-style: none;
    font-family: "Roboto Condensed", sans-serif; font-size: 32px; color: var(--navy); line-height: 42px;
  }
  .slogan li::before {
    content: ""; display: inline-block; width: 7px; height: 7px; background: var(--green);
    transform: rotate(45deg); margin: 0 8px 6px 0; vertical-align: middle;
  }
  .tagline {
    position: absolute; left: 20px; top: 345px; width: 420px;
    font-family: "Arimo", sans-serif; font-style: italic; font-weight: 700;
    font-size: 28px; line-height: 38px; color: var(--ink); text-align: center;
    transform: rotate(-6deg); white-space: nowrap;
  }
  .tagline span { display: block; }
  .contact { position: absolute; left: 30px; top: 512px; width: 402px; text-align: center; font-family: "Montserrat", sans-serif; font-weight: 800; color: var(--navy); }
  .contact .phone { font-size: 31px; }
  .contact .address { font-size: 16.5px; margin-top: 8px; letter-spacing: 0.2px; white-space: nowrap; }
  .patient-group {
    position: absolute; left: 456px; width: 124px; height: 124px; border-radius: 50%;
    background: var(--paper); border: 8px solid var(--green);
  }
  .patient-group .art {
    position: absolute; inset: 10px; border-radius: 50%;
    background: radial-gradient(circle, #5a5a5a 0%, #d8d8d8 70%, #ffffff 100%);
  }
  .group-infant { top: 160px; }
  .group-family { top: 303px; }
  .group-senior { top: 445px; }
</style>
</head>
<body>
<div class="canvas">
  <section class="ad">
    <div class="side-band"></div>

    <h1 class="practice-name">
      <span class="line-main">Hale &amp; Whitcombe</span>
      <span class="line-sub">Family Practice</span>
    </h1>
    <div class="name-mark"></div>

    <ul class="slogan">
      <li>Restore</li>
      <li>Refresh</li>
      <li>Renew</li>
    </ul>

    <p class="tagline"><span>Proudly looking</span><span>after you &amp; your family</span><span>for almost 20 years.</span></p>

    <div class="contact">
      <p class="phone">Ph: 568-9072</p>
      <p class="address">47 FENNEL LANE, SOUTHAMPTON TQ19</p>
    </div>

    <div class="patient-group group-infant"><div class="art" role="img" aria-label="Icon of a baby bodysuit with a heart"></div></div>
    <div class="patient-group group-family"><div class="art" role="img" aria-label="Icon of two parents holding a child's hands"></div></div>
    <div class="patient-group group-senior"><div class="art" role="img" aria-label="Icon of an elderly couple with walking canes"></div></div>
  </section>
</div>
</body>
</html>
```